The Copper Lantern illustrated story adaptation design

I need a graphic-novel-style design of the 10-page story, “The Copper Lantern.” This will appear in a collection of graphic-novel-style adaptations of stories which I am posting online (and printing) in May.

Half of the files are on stashbin (under "6 images"):

https://www.stashbin.net/s/3kqm218x45trwz9/page%20thumbs_0full_01.jpg?dl=0

Target Market(s)

comic book readers, graphic novel readers, young adult readers

Industry/Entity Type

Publishing

Font styles to use
Serif
Other font styles liked:
• Caslon Anitque, Californian FB, 1584 Pragmatica Lima

Colors

Designer to choose colors to be used in the design.

Requirements
Must have
• A bold design scheme !! The art and text are solid, but they certainly need a clever design concept that can bind the project together.
Nice to have
• An inviting, reader-friendly background of some kind (I offer suggestions in my notes).
Should not have
• Hard-to-read graphics

```html
<!DOCTYPE html>
<html lang="en">
<head>
<meta charset="utf-8">
<title>The Copper Lantern – Page 5</title>
<link rel="stylesheet" href="https://fonts.googleapis.com/css2?family=Gentium+Book+Plus:wght@400;700&display=swap">
<style>
  :root {
    --canvas: #ffffff;
    --stone-light: #a9a1ad;
    --stone-mid: #8c8393;
    --stone-dark: #6f6676;
    --frame: #000000;
    --night-deep: #1c1540;
    --night-blue: #3a3a8c;
    --night-teal: #3f6f8a;
    --night-magenta: #b2397f;
    --panel: rgba(235, 232, 238, 0.72);
    --ink: #1e1a22;
    --header-ink: #ffffff;
  }
  * { box-sizing: border-box; margin: 0; padding: 0; }
  html, body {
    width: 1200px;
    height: 1200px;
    overflow: hidden;
    background: var(--canvas);
  }
  .page {
    position: absolute;
    left: 172px;
    top: 68px;
    width: 856px;
    height: 1064px;
    background:
      radial-gradient(ellipse at 20% 65%, rgba(200,190,205,0.55), transparent 45%),
      radial-gradient(ellipse at 75% 20%, rgba(190,185,195,0.5), transparent 40%),
      radial-gradient(ellipse at 60% 90%, rgba(95,85,105,0.45), transparent 50%),
      linear-gradient(160deg, var(--stone-light), var(--stone-mid) 55%, var(--stone-dark));
    font-family: "Gentium Book Plus", "Palatino Linotype", serif;
  }
  .running-head {
    position: absolute;
    top: 56px;
    left: 70px;
    right: 72px;
    display: flex;
    justify-content: space-between;
    color: var(--header-ink);
    font-weight: 700;
    font-size: 16px;
    letter-spacing: 0.2px;
  }
  .illustration-frame {
    position: absolute;
    left: 65px;
    top: 98px;
    width: 726px;
    height: 462px;
    background: var(--frame);
    padding: 10px;
  }
  .illustration {
    width: 100%;
    height: 100%;
    background:
      radial-gradient(ellipse at 30% 55%, rgba(178,57,127,0.7), transparent 30%),
      radial-gradient(ellipse at 42% 30%, rgba(63,111,138,0.8), transparent 35%),
      radial-gradient(ellipse at 75% 55%, rgba(20,12,40,0.9), transparent 45%),
      linear-gradient(135deg, var(--night-blue), var(--night-deep));
  }
  .story-panel {
    position: absolute;
    left: 65px;
    top: 664px;
    width: 726px;
    height: 308px;
    background: var(--panel);
    padding: 42px 28px 0 28px;
    color: var(--ink);
    font-size: 16.4px;
    line-height: 21px;
  }
  .story-panel p {
    text-indent: 24px;
    margin-bottom: 9px;
  }
</style>
</head>
<body>
  <article class="page">
    <header class="running-head">
      <span class="page-number">Page 5</span>
      <span class="story-title">The Copper Lantern</span>
    </header>

    <figure class="illustration-frame">
      <div class="illustration" role="img" aria-label="Painted scene in deep violet and blue: an armoured swordsman stands in a stone passage facing a dark shield-bearing figure, lit by magenta glow"></div>
    </figure>

    <section class="story-panel">
      <p>With a low laugh, he stepped into the center of the passageway.</p>
      <p>“Come, brothers,” he bellowed. He banged his blade against the stone wall. “Here is better sport.”</p>
      <p>He rushed the soldiers.</p>
      <p>The sword in his hand flashed: he gutted the largest member of the guard. Before that body struck the stone floor, his gleaming blade severed the second man’s head: the third he grabbed by the neck and, lifting a corded arm, snapped the man’s neck. The fourth and fifth guardsmen held back. He motioned for them to advance. They fled. Snatching a blade from the dead man, he flung it and saw the fourth man fall gurgling to the stone floor.</p>
    </section>
  </article>
</body>
</html>
```